To design the Curriculum Vitae of a General Manager Legal

the objective is to redesign the attached Résumé for a senior level Internal Legal Executive in order to make it attractive, easily readable, catchy, modern looking while staying classy, elegant, sobre, and serious.
The résumé is attached to this project. it contains the followings sections : Photo; Contact Details; Summary; Education; Experience; Other.
Feel free to use photoshop to improve photo.
Updates

Target Market(s)

Legal community; law firms; Big corporations requiring internal legal senior executive

Font styles to use
Serif

Colors
ffffff
85cae6
33a6d7
0292cd
86cfc6
cfeae6
757575
919191
d9d9d9

Requirements
Must have
• classy; serious; professional; elegant; easy to read; catchy; modern;

```html
<!DOCTYPE html>
<html lang="en">
<head>
<meta charset="utf-8">
<title>Resume – Lina Haddad Morel</title>
<link href="https://fonts.googleapis.com/css2?family=Crimson+Text:ital,wght@0,400;1,400&family=Open+Sans:wght@300;400&family=Roboto+Condensed:wght@400&display=swap" rel="stylesheet">
<style>
  :root{
    --paper:#ffffff;
    --backdrop:#ffffff;
    --teal-text:#12a487;
    --bar-light:#6cc4bd;
    --bar-dark:#346f6c;
    --title-faint:#dff1ee;
    --ink:#1d1d1d;
    --grey:#757575;
    --rule:#d9d9d9;
    --photo-top:#cfeae6;
    --photo-mid:#9a6a55;
  }
  *{box-sizing:border-box;margin:0;padding:0}
  html,body{width:1200px;height:884px;overflow:hidden;background:var(--backdrop)}
  .canvas{position:relative;width:1200px;height:884px}
  .page{position:absolute;top:36px;width:574px;height:812px;background:var(--paper);
        box-shadow:0 0 10px rgba(0,0,0,.12);overflow:hidden}
  .page--one{left:13px}
  .page--two{left:607px}

  .doc-title{position:absolute;left:48px;top:24px;font:300 72px/1 "Open Sans",sans-serif;
             color:var(--title-faint);letter-spacing:-2px}
  .name{position:absolute;left:88px;top:118px;font:300 22px/1 "Open Sans",sans-serif;color:#555}
  .contact{position:absolute;left:88px;top:148px;font:400 10px/14px "Roboto Condensed",sans-serif;color:var(--bar-dark)}
  .photo{position:absolute;left:420px;top:26px;width:110px;height:136px;
         background:linear-gradient(160deg,var(--photo-top) 0%,#b9dcd6 45%,var(--photo-mid) 100%)}

  .side-bar{position:absolute;left:88px;width:26px}
  .side-bar span{position:absolute;left:5px;top:10px;writing-mode:vertical-rl;
                 font:400 14px/1 "Open Sans",sans-serif;color:#fff;letter-spacing:1px}
  .side-bar--summary{top:195px;height:362px;background:var(--bar-light)}
  .side-bar--education{top:580px;height:190px;background:var(--bar-dark)}
  .side-bar--experience{left:87px;top:42px;height:723px;background:var(--bar-dark)}

  .summary{position:absolute;left:227px;top:191px;width:306px;
           font:italic 400 11px/14.5px "Crimson Text",serif;color:var(--ink);text-align:justify}
  .summary p{text-indent:14px;margin-bottom:10.5px}

  .block{position:absolute}
  .school{font:400 14.5px/18px "Open Sans",sans-serif;color:var(--teal-text);white-space:nowrap}
  .dotted{list-style:none}
  .dotted li{font:400 11px/14.5px "Crimson Text",serif;color:var(--ink);
             text-align:justify;margin-bottom:8px;position:relative}
  .dotted li::before{content:"";position:absolute;left:-18px;top:6px;
             width:3px;height:3px;border-radius:50%;background:var(--ink)}
  .edu-text{left:227px;width:306px}
  .edu-head{left:164px}

  .page-footer{position:absolute;left:50px;right:40px;top:785px;border-top:1px solid var(--rule);
               padding-top:6px;display:flex;justify-content:space-between;
               font:400 9px/1 "Open Sans",sans-serif;color:var(--grey)}
  .page-footer span:first-child{padding-left:8px}
  .page-footer span:last-child{padding-right:12px}

  .period{left:137px;width:396px;font:300 13px/16px "Open Sans",sans-serif;color:var(--grey);
          border-bottom:1px solid var(--rule);padding-bottom:2px}
  .role{left:164px;width:370px;font:400 14.5px/18px "Open Sans",sans-serif;color:var(--teal-text)}
  .label{left:205px;font:300 13px/16px "Open Sans",sans-serif;color:var(--grey)}
  .subhead{left:205px;font:400 12.5px/16px "Crimson Text",serif;color:var(--teal-text)}
  .body-text{left:226px;width:307px;font:400 11px/14.5px "Crimson Text",serif;color:var(--ink);text-align:justify}
</style>
</head>
<body>
<div class="canvas">

  <section class="page page--one">
    <h1 class="doc-title">RESUME</h1>
    <div class="name">Lina Haddad Morel</div>
    <div class="contact">mobile : +971 50 123 4567<br>e-mail : lina.haddad@mail.com</div>
    <div class="photo" role="img" aria-label="Portrait photograph of the candidate"></div>

    <div class="side-bar side-bar--summary"><span>SUMMARY</span></div>
    <div class="summary">
      <p>A senior qualified legal professional with more than 15 years of experience in private practice and in-house focusing on the following industries: Real Estate, Retail and Services, obtained in UAE, France and Syria. Practice transactional skills (M&amp;A, real estate, commercial, corporate restructuring, strategic funding), organizational skills (policies and procedures and authority matrix covering different contexts in corporate environment), lawyering skills (preemptive legal advice, and a multi jurisdiction litigation management expertise), managerial skills (enhancing the value add of the legal department as both a service provider and a risk gatekeeper).</p>
      <p>Joined Noor Al Waha Group in November 2011, an internationally recognized industry Leader in shopping malls, communities, retail and leisure across the Middle East, Africa and Asia, first as Legal Counsel at Noor Al Waha Properties responsible for UAE Shopping Malls, Project management and communities, and then moved in Mai 2015 to Noor Al Waha Retail -Hypermart where currently I occupy the role of GM-Legal, focusing mainly on leading and managing the legal, compliance and risk management strategies across a wide geographic area of countries.</p>
      <p>Prior to moving to Dubai, I have lived in Paris France, where I have worked in various organizations including the Global Chamber Arbitration Court, a billing software company and a consultancy practice. I graduated from Meridian University of Law with two Master Degrees.</p>
      <p>Mother of Three, I am passionate about Bon Fide work towards Women Empowerment and Refugee Children Education.</p>
    </div>

    <div class="side-bar side-bar--education"><span>EDUCATION</span></div>
    <h3 class="block school edu-head" style="top:585px">Meridian University of Law (Paris) Paris – France</h3>
    <ul class="block dotted edu-text" style="top:613px">
      <li>Master degree in Litigation, Arbitration, and Alternative Dispute Resolution (98- 99)</li>
      <li>Master degree in commercial law (97-98)</li>
    </ul>
    <h3 class="block school edu-head" style="top:678px">Institute of Applied Legal Studies Paris - France (97-98)</h3>
    <h3 class="block school edu-head" style="top:712px">Levant National University – Syria</h3>
    <ul class="block dotted edu-text" style="top:741px"><li>Law degree (92-96)</li></ul>

    <footer class="page-footer"><span>1 |</span><span>RESUME - Lina Haddad Morel</span></footer>
  </section>

  <section class="page page--two">
    <div class="side-bar side-bar--experience"><span>EXPERIENCE</span></div>

    <div class="block period" style="top:44px">April 2017 - Present</div>
    <h3 class="block role" style="top:71px">General Manager Legal at Noor Al Waha- Hypermart<br>(“NAWH”)</h3>

    <div class="block period" style="top:130px">May 2015 - April 2017</div>
    <h3 class="block role" style="top:157px">Senior Legal Counsel at Noor Al Waha Retail Hypermart</h3>

    <div class="block label" style="top:188px">Description of Position</div>
    <p class="block body-text" style="top:213px">Lead and manage the legal, compliance, functions and risk management function for NAWH operations in Syria, Lebanon, Jordan, Iraq, Egypt, Georgia, Armenia and Pakistan (“Countries”). A Legal Business Partner to drive business development agenda (organically, M&amp;A, digital/ ecommerce), and contribute to functional strategies.</p>

    <div class="block label" style="top:302px">Key Responsibilities</div>
    <div class="block subhead" style="top:332px">Legal Division Leadership</div>
    <ul class="block dotted body-text" style="top:357px">
      <li>Develop and execute the legal strategy and plans in alignment with strategic objectives of the company</li>
      <li>Lead the Legal team across the Countries: attract, develop, assess and engage the right legal talents</li>
      <li>Coordinating with management and Head of business units, evaluating strategy and merits and or progress of specific projects.</li>
      <li>Manage and coordinate the Company’s approach towards litigation to ensure cost effectiveness including negotiations of contracts with outside legal firms, monitor quality of work and delivery</li>
    </ul>
    <div class="block subhead" style="top:522px">M&amp;A:</div>
    <p class="block body-text" style="top:544px">Contribute to M&amp;A and prospective acquisitions activities, perform due diligence, terms negotiations, closing and post-closing tasks</p>
    <div class="block subhead" style="top:589px">Business Development/Partnership</div>
    <ul class="block dotted body-text" style="top:614px">
      <li>Lead &amp; implement the legal expansion plans in Countries including setting up new legal entities, due diligence, and risk matrix</li>
      <li>Prepare and structure complex contract negotiations. Examine intricate agreements and other documents for accuracy, legality and conformity with business standards:</li>
      <li>Oversee the legal process Prepare and review agreements, contracts regarding commercial , development and business transactions: Memoranda of Understanding, Agreements to Lease and Lease Agreement, JVs, Franchise Agreements, Consultancy Agreements,</li>
    </ul>

    <footer class="page-footer"><span>2 |</span><span>RESUME - Lina Haddad Morel</span></footer>
  </section>

</div>
</body>
</html>
```